Brochure design for 3D ultrasound company

I am looking for a clean and modern and edgy brochure for my ultrasound company. We are a fairly new company specialize in 3D/4D ultrasounds.Our brochures will be placed in OB-GYN offices in high end areas around Los Angeles, so we need something that will stand out and capture a modern woman's attention. Our logo is currently in the process of being designed, so I don't have a picture to provide quite yet, however it will be our company name"Kite + Fern" written in a special font that looks like neon lights. I will attach a few images of what our logo will be like, and some initial content that can help provide the layout we would like for the brochure. please feel free to also take a look at our website. www.kitefernscans.example.

Target Market(s)

Upscale trendy women.

Colors
eea4c8
33a6d7
fee18a

Requirements
Should not have
• too many colors.

```html
<!DOCTYPE html>
<html lang="en">
<head>
<meta charset="utf-8">
<title>Kite + Fern – Trifold Brochure</title>
<link href="https://fonts.googleapis.com/css2?family=Montserrat:wght@400;500;600;700;800&display=swap" rel="stylesheet">
<style>
:root{
  --pink:#eea4c8;
  --pink-deep:#e489b5;
  --blue:#33a6d7;
  --yellow:#fee18a;
  --ink:#2b2b2b;
  --paper:#ffffff;
  --stage:#33603f;
}
*{box-sizing:border-box;margin:0;padding:0}
html,body{width:818px;height:1200px;overflow:hidden}
body{background:var(--stage);font-family:'Montserrat',sans-serif;color:var(--ink);position:relative}
.sheet{position:absolute;left:93px;width:632px;height:488px;overflow:hidden;background:var(--yellow)}
.sheet--outside{top:58px}
.sheet--inside{top:635px}
.backdrop{position:absolute;inset:0}
.card{position:absolute;background:var(--paper);overflow:hidden}
.photo{position:absolute}
.tri{position:absolute}
/* outside, panel one */
.explain{left:9px;top:9px;width:193px;height:470px}
.explain__title{color:var(--pink);font-weight:800;font-size:16px;text-align:center;margin-top:14px;letter-spacing:.5px}
.explain__body{padding:6px 10px 0 10px;font-size:7.6px;line-height:16.5px;text-align:justify}
.explain__body p{text-indent:22px;margin-bottom:6px}
.explain__body b{font-weight:700}
.explain__photo{left:0;top:342px;width:193px;height:128px;background:linear-gradient(180deg,#f4f2f0,#e6d5cc 55%,#3a3a3a)}
/* outside, panel two */
.about{left:220px;top:9px;width:192px;height:470px;text-align:center}
.about__map{left:6px;top:8px;width:180px;height:128px;background:radial-gradient(ellipse at 65% 70%,#efe6d4 0,#f7f3ea 45%,#fff 75%)}
.about__text{position:absolute;top:166px;left:6px;right:6px;font-size:7px;line-height:14.9px}
.brand{font-weight:600;color:var(--pink);letter-spacing:1px}
.about__brand{position:absolute;top:322px;left:0;right:0;font-size:22px}
.about__tag{position:absolute;top:352px;left:0;right:0;font-size:8px;font-weight:700;color:var(--blue)}
.about__contact{position:absolute;top:382px;left:0;right:0;font-size:8px;line-height:14.5px}
/* outside, cover */
.cover__photo{left:422px;top:0;width:210px;height:330px;background:linear-gradient(180deg,#e9e6e2,#d6c4b6 45%,#c9a58f 70%,#e8e3dd)}
.cover__shapes{position:absolute;left:422px;top:0}
.cover__brand{position:absolute;left:422px;width:210px;top:378px;text-align:center;font-size:24px;color:var(--paper)}
.cover__tag{position:absolute;left:422px;width:210px;top:411px;text-align:center;font-size:7.6px;font-weight:700;color:var(--paper)}
.cover__band{position:absolute;left:422px;width:210px;top:427px;height:29px;background:var(--pink-deep);color:#fff;text-align:center;font-size:9px;line-height:13px;padding-top:2px}
.cover__call{position:absolute;left:422px;width:210px;top:460px;text-align:center;font-size:11px;color:#fff}
.cover__call b{font-weight:700}
/* inside, panel one */
.popular{left:9px;top:9px;width:193px;height:470px}
.popular__photo{left:0;top:0;width:193px;height:134px;background:radial-gradient(circle at 50% 45%,#f3eaea 0,#f3a6a8 38%,#c98d86 60%,#7b8a6a 100%)}
.popular__title{position:absolute;top:172px;left:0;right:0;text-align:center;color:var(--pink);font-weight:800;font-size:13.5px;line-height:17px}
.popular__name{position:absolute;top:212px;left:15px;font-weight:800;font-size:10.5px}
.popular__list{position:absolute;top:227px;left:15px;list-style:none;font-size:7.8px;line-height:17.8px}
.popular__list li::before{content:"• ";color:var(--pink)}
.callout{position:absolute;left:9px;width:175px;height:33px;border-left:1px solid var(--pink);border-right:1px solid var(--pink);text-align:center;font-size:10.5px;line-height:16px;padding-top:1px}
.callout::before{content:"";position:absolute;left:0;right:0;height:33px;top:0;border-top:1px solid var(--pink);border-bottom:1px solid var(--pink);clip-path:polygon(0 0,6px 0,6px 100%,0 100%,0 0,100% 0,100% 100%,calc(100% - 6px) 100%,calc(100% - 6px) 0,100% 0)}
.callout--1{top:343px}.callout--2{top:386px}.callout--3{top:430px}
/* inside, services */
.services-head{left:220px;top:9px;width:402px;height:74px;text-align:center}
.services-head__title{color:var(--pink);font-weight:800;font-size:19px;letter-spacing:2.5px;margin-top:10px}
.services-head__sub{font-size:10.5px;line-height:16px;margin-top:2px}
.pkg{left:220px;width:402px;height:122px}
.pkg--1{top:93px}.pkg--2{top:225px}.pkg--3{top:357px}
.pkg__title{position:absolute;top:9px;color:var(--pink);font-weight:800;font-size:14px;letter-spacing:.3px;white-space:nowrap}
.pkg__title small{font-size:8px;letter-spacing:0}
.pkg__list{position:absolute;list-style:none;font-size:9px;line-height:19.5px}
.pkg__list li::before{content:"• "}
.pkg--3 .pkg__title{font-size:12.5px;letter-spacing:0}
.pkg--3 .pkg__list{line-height:14.4px}
.pkg__photo{top:0;width:152px;height:122px}
.pkg__photo--belly{background:linear-gradient(180deg,#f4f2f0,#e6d0c2 50%,#d3a98e 75%,#3a3a3a)}
.pkg__photo--plush{background:linear-gradient(160deg,#f2efec,#e8c7b0 60%,#f4f0ec)}
.pkg__photo--couple{background:linear-gradient(160deg,#e9c8b4,#c9d6e4 55%,#5a7697)}
</style>
</head>
<body>

<!-- Outside of the brochure -->
<section class="sheet sheet--outside">
  <svg class="backdrop" width="632" height="488" viewBox="0 0 632 488">
    <rect width="632" height="488" fill="var(--yellow)"/>
    <polygon points="0,488 0,240 211,120 211,488" fill="var(--blue)"/>
    <polygon points="150,488 211,455 211,488" fill="var(--yellow)"/>
    <polygon points="211,350 422,0 422,350" fill="var(--blue)"/>
    <polygon points="211,488 211,470 290,488" fill="var(--blue)"/>
  </svg>

  <div class="card explain">
    <h2 class="explain__title">WHAT’S WHAT...</h2>
    <div class="explain__body">
      <p><b>2D</b> is the traditional black and white photo– you know, the one that you want to get emotional about, but you don’t know what you’re looking at.</p>
      <p><b>3D</b> is an image of the fetus and it’s features. So you can see the baby has dad’s nose, and mom’s lips.</p>
      <p><b>4D</b> is 3D, but with motion. You can see the baby yawn, move it’s arm, or even give you a smile.</p>
      <p><b>HD</b> is also 3D, but better. Now you can see a rendering of the baby’s skin making it the most realistic fetal image possible.. we are one of the few in Los Angeles that have the newest HD capable machines</p>
    </div>
    <svg class="tri" style="left:52px;top:313px" width="88" height="20"><polygon points="44,0 88,20 0,20" fill="var(--pink)"/></svg>
    <div class="photo explain__photo" role="img" aria-label="Photo of a pregnant belly with hands holding an ultrasound print"></div>
  </div>

  <div class="card about">
    <div class="photo about__map" role="img" aria-label="Faint map of an island chain"></div>
    <svg class="tri" style="left:52px;top:138px" width="88" height="20"><polygon points="0,0 88,0 44,20" fill="var(--pink)"/></svg>
    <p class="about__text">Kite + Fern is a mobile 3D ultrasound company servicing Los Angeles, and surrounding areas. We take great pride in being one of LA’s first mobile Ultrasound companies and for being an all female business!<br>Our mission is to provide an unforgettable experience for expectant mothers in the comfort of their home!</p>
    <div class="brand about__brand">KITE + FERN</div>
    <div class="about__tag">A mobile 3D/4D ultrasound service</div>
    <div class="about__contact">
      Telephone: (310) 555-0147<br>
      www.kitefernscans.example<br>
      Email: hello@kitefernscans.example<br>
      Instagram: kite_fern<br>
      Facebook: @kitefernscans
    </div>
  </div>

  <div class="photo cover__photo" role="img" aria-label="Photo of a pregnant woman on a bed holding an ultrasound strip"></div>
  <svg class="cover__shapes" width="210" height="488" viewBox="0 0 210 488">
    <polygon points="0,210 0,330 60,330" fill="var(--yellow)" opacity=".75"/>
    <polygon points="0,270 0,330 210,330 210,210 120,300" fill="var(--blue)" opacity=".8"/>
    <polygon points="130,330 210,285 210,330" fill="var(--pink)" opacity=".8"/>
    <polygon points="0,330 0,388 100,330" fill="var(--blue)"/>
    <polygon points="0,388 100,330 210,390 210,488 0,488" fill="var(--pink)"/>
    <polygon points="100,330 210,330 210,390" fill="var(--yellow)"/>
  </svg>
  <div class="brand cover__brand">KITE + FERN</div>
  <div class="cover__tag">A mobile 3D/4D ultrasound service</div>
  <div class="cover__band">ULTRASOUND IN THE<br>COMFORT OF YOUR HOME.</div>
  <div class="cover__call">call today! <b>310-555-0147</b></div>
</section>

<!-- Inside of the brochure -->
<section class="sheet sheet--inside">
  <svg class="backdrop" width="632" height="488" viewBox="0 0 632 488">
    <rect width="632" height="488" fill="var(--blue)"/>
    <polygon points="0,0 211,0 211,80 0,200" fill="var(--yellow)"/>
    <polygon points="140,488 211,455 211,488" fill="var(--yellow)"/>
    <polygon points="211,0 422,0 211,100" fill="var(--yellow)"/>
    <polygon points="211,88 260,88 211,110" fill="var(--yellow)"/>
    <polygon points="560,220 632,185 632,220" fill="var(--yellow)"/>
    <polygon points="330,488 632,488 632,352 400,488" fill="var(--yellow)"/>
  </svg>

  <div class="card popular">
    <div class="photo popular__photo" role="img" aria-label="Photo of a pregnant woman in white among pink smoke"></div>
    <svg class="tri" style="left:52px;top:143px" width="88" height="19"><polygon points="0,0 88,0 44,19" fill="var(--pink)"/></svg>
    <h2 class="popular__title">OUR MOST POPULAR<br>PACKAGE</h2>
    <h3 class="popular__name">THE BIG REVEAL!! $225.00</h3>
    <ul class="popular__list">
      <li>25 minute 3D/4D/HD live session</li>
      <li>5 black and white pictures</li>
      <li>5 color pictures</li>
      <li>Email or USB flash drive with all images</li>
      <li>Record and hear heartbeat</li>
      <li>Confirm gender</li>
    </ul>
    <p class="callout callout--1">Ready for your baby’s first<br>photoshoot?</p>
    <p class="callout callout--2">Give us a call to schedule an<br>appointment (310) 555-0147</p>
    <p class="callout callout--3">or visit our website<br>www.kitefernscans.example</p>
  </div>

  <div class="card services-head">
    <h2 class="services-head__title">SERVICES + PRICING</h2>
    <p class="services-head__sub">We are available for private in-home screenings, gender<br>reveals, baby showers, or any other special occasion!</p>
  </div>

  <div class="card pkg pkg--1">
    <h3 class="pkg__title" style="left:12px">PEEK-A-BOO <span style="margin-left:30px">$ 125.00</span></h3>
    <ul class="pkg__list" style="left:12px;top:40px">
      <li>15 minute 2D session</li>
      <li>3 black and white images</li>
      <li>Listen to baby’s heartbeat</li>
      <li>Confirm gender</li>
    </ul>
    <svg class="tri" style="left:222px;top:16px" width="20" height="88"><polygon points="20,0 20,88 0,44" fill="var(--pink)"/></svg>
    <div class="photo pkg__photo pkg__photo--belly" style="left:250px" role="img" aria-label="Photo of hands holding an ultrasound print on a belly"></div>
  </div>

  <div class="card pkg pkg--2">
    <div class="photo pkg__photo pkg__photo--plush" style="left:0" role="img" aria-label="Photo of a pregnant belly with a plush toy"></div>
    <svg class="tri" style="left:163px;top:18px" width="20" height="86"><polygon points="0,0 20,43 0,86" fill="var(--pink)"/></svg>
    <h3 class="pkg__title" style="left:190px">HELLO, MOMMA <span style="margin-left:8px">$165.00</span></h3>
    <ul class="pkg__list" style="left:190px;top:38px;line-height:16.8px">
      <li>15 minute 3D/4D /HD live session</li>
      <li>3 black and white images</li>
      <li>2 color images</li>
      <li>Listen to baby’s heartbeat</li>
      <li>Confirm gender</li>
    </ul>
  </div>

  <div class="card pkg pkg--3">
    <h3 class="pkg__title" style="left:12px">V.I.B <small>(VERY IMPORTANT BABY)</small> <span style="margin-left:3px">$325.00</span></h3>
    <ul class="pkg__list" style="left:12px;top:36px">
      <li>30 min 3D/4D/HD live session<br>&nbsp;&nbsp;on our projector</li>
      <li>10 color images</li>
      <li>Email or USB with all images</li>
      <li>Record and hear heartbeat</li>
      <li>Confirm gender</li>
    </ul>
    <svg class="tri" style="left:222px;top:16px" width="20" height="88"><polygon points="20,0 20,88 0,44" fill="var(--pink)"/></svg>
    <div class="photo pkg__photo pkg__photo--couple" style="left:250px" role="img" aria-label="Photo of a couple holding boy and girl notes over a belly"></div>
  </div>
</section>

</body>
</html>
```